TORVEL Business Card Design

We need a business card design for a current Plastering company now moving to building and constructing new homes.
We have been in the Plastering(rendering) business for 15yrs and have made a good name with our customers for our Top Quality of work that we provide.
We would like TORVEL to be the main attraction with an image of architectural roof tops or house design within it. Blue Yellow and Black are colours we like but are willing to see other ideas.
We would like the design to be modern and communicate quality and experience.
Industry/Entity Type
Building
Contact Information for Business Card
TORVEL Building and Plastering
PO BOX 57390 Marlowe Darwin NT 0815
PH/Fax: 08 89317725 Email: torvel@quellnet.com
Dale: 0417396248 Rosa:0409273516
ABN:58 297 130 846

```html
<!DOCTYPE html>
<html lang="en">
<head>
<meta charset="utf-8">
<title>TORVEL Building and Plastering – Business Card</title>
<link href="https://fonts.googleapis.com/css2?family=Questrial&family=Open+Sans:wght@400&display=swap" rel="stylesheet">
<style>
  :root {
    --stage-centre: #ffffff;
    --stage-edge: #eeeff0;
    --card: #e3e4e4;
    --ink: #111111;
    --dash: #555555;
    --brick: #cdcaca;
    --brick-edge: #bdb9b9;
  }
  * { margin: 0; padding: 0; box-sizing: border-box; }
  html, body { width: 1200px; height: 1000px; overflow: hidden; }
  body {
    position: relative;
    background: radial-gradient(ellipse at 50% 50%, var(--stage-centre) 0%, var(--stage-centre) 30%, var(--stage-edge) 100%);
    color: var(--ink);
  }
  .card {
    position: absolute;
    left: 307px;
    width: 629px;
    height: 352px;
    background: var(--card);
    border-radius: 10px;
  }
  .card--front { top: 116px; }
  .card--back { top: 550px; }
  .card__trim {
    position: absolute;
    left: 20px; top: 15px; right: 20px; bottom: 14px;
    border: 1.5px dashed var(--dash);
    border-radius: 10px;
  }
  .brick {
    position: absolute;
    width: 81px; height: 34px;
    background: var(--brick);
    box-shadow: inset 0 0 0 1px var(--brick-edge);
  }
  .brand-name {
    position: absolute;
    left: 0; right: 0; top: 44px;
    text-align: center;
    font-family: "Questrial", sans-serif;
    font-size: 96px;
    letter-spacing: 2px;
    line-height: 1;
    color: var(--ink);
  }
  .brand-tagline {
    position: absolute;
    left: 0; right: 0; top: 155px;
    padding-left: 14px;
    text-align: center;
    font-family: "Questrial", sans-serif;
    font-size: 24px;
    line-height: 1;
  }
  .back-title {
    position: absolute;
    left: 0; right: 0; top: 68px;
    padding-left: 18px;
    text-align: center;
    font-family: "Questrial", sans-serif;
    font-size: 28px;
    line-height: 1;
  }
  .back-rule {
    position: absolute;
    left: 33px; top: 134px;
    width: 563px; height: 9px;
    background: var(--ink);
  }
  .contact-list {
    position: absolute;
    list-style: none;
    font-family: "Open Sans", sans-serif;
    font-size: 16.5px;
    line-height: 21px;
  }
  .contact-list li { position: relative; padding-left: 17px; }
  .contact-list li::before {
    content: "";
    position: absolute;
    left: 0; top: 7px;
    width: 7px; height: 7px;
    border-radius: 50%;
    background: var(--ink);
  }
  .contact-list li.continued::before { display: none; }
  .contact-list--postal { left: 33px; top: 192px; }
  .contact-list--people { left: 397px; top: 193px; line-height: 26px; }
  .contact-list--people li::before { top: 9px; }
  .contact-list--people li.abn { margin-top: 4px; }
</style>
</head>
<body>

  <section class="card card--front" aria-label="Card front">
    <div class="card__trim"></div>
    <div class="brick-group" role="img" aria-label="Textured brick blocks">
      <span class="brick" style="left:23px; top:65px;"></span>
      <span class="brick" style="left:49px; top:106px;"></span>
      <span class="brick" style="left:23px; top:145px;"></span>
      <span class="brick" style="left:490px; top:203px; width:80px;"></span>
      <span class="brick" style="left:431px; top:242px;"></span>
      <span class="brick" style="left:522px; top:242px; width:82px;"></span>
      <span class="brick" style="left:462px; top:284px;"></span>
    </div>
    <h1 class="brand-name">TORVEL</h1>
    <p class="brand-tagline">Building and Plastering</p>
  </section>

  <section class="card card--back" aria-label="Card back">
    <div class="card__trim"></div>
    <h2 class="back-title">TORVEL Building and Plastering</h2>
    <div class="back-rule"></div>
    <ul class="contact-list contact-list--postal">
      <li>PO BOX 57390 Marlowe Darwin</li>
      <li class="continued">NT 0815 PH</li>
      <li>Fax: 08 89317725</li>
      <li>Email: torvel@quellnet.com</li>
    </ul>
    <ul class="contact-list contact-list--people">
      <li>Dale: 0417396248</li>
      <li>Rosa:0409273516</li>
      <li class="abn">ABN:58 297 130 846</li>
    </ul>
  </section>

</body>
</html>
```